A start up ecommerce site. Selling one item at the moment and hope to expand. Selling acrylic makeup organizers. It is a product for women. It stores all cosmetic/makeup.... a storage solution.
Its a womens product so it should be geared towards it. I have a logo that I will upload.
My shop: http://www.crafterlane.com/shop/VanityNookBoxes
Not the best photos, so if you know how to touch up it would be a plus.

I don't sell makeup.

competitors sites

http://www.thelumenvault.com/#info

http://www.prismbeautybin.com/

http://maudiepetal.com/

http://lumenvaultstorage.com/

 

Reason: Out of town. Please continue to leave question and designs.

Target Market(s)

Women

Industry/Entity Type

Shop

Requirements
Must have
• Social Media Logos. Chirply,Friendwall,Searchly+ and Pinvora Like Buttons
Cashwagons/Pendo
Shopping Cart
Main page with the product and description. Buy Now or add to cart button. Our policy, contact us, email register.
Nice to have
• Fun, Modern, Girly. Not over complicated and easy to navigate, simple.
Should not have
• Anything from the competitor.

```html
<!DOCTYPE html>
<html lang="en">
<head>
<meta charset="utf-8">
<title>vanitynook – Crystal Tier Acrylic Makeup Organizer</title>
<link rel="stylesheet" href="https://fonts.googleapis.com/css2?family=Nunito+Sans:wght@200;300;400;600;700&display=swap">
<style>
  :root {
    --pink: #e4577f;
    --pink-dark: #c94269;
    --ink: #444446;
    --ink-soft: #5a5a5c;
    --grey-text: #8c8c8e;
    --header-top: #f1f1f2;
    --header-bottom: #c9c9cb;
    --nav-bg: #fdfdfd;
    --hero-dark: #0c0c0d;
    --hero-mid: #3a3a3c;
    --lower-bg: #d8d8d9;
    --card-bg: #f4f4f5;
    --rule: #d6d6d8;
    --footer-icon: #9d9d9f;
    --button-dark: #59595b;
  }
  * { box-sizing: border-box; margin: 0; padding: 0; }
  html, body { width: 1200px; height: 816px; overflow: hidden; }
  body {
    font-family: "Nunito Sans", Helvetica, Arial, sans-serif;
    color: var(--ink);
    background: var(--lower-bg);
    position: relative;
  }
  a { color: inherit; text-decoration: none; }

  .site-header {
    position: absolute; left: 0; top: 0; width: 1200px; height: 86px;
    background: radial-gradient(ellipse at 50% 40%, var(--header-top) 0%, #dcdcdd 55%, var(--header-bottom) 100%);
    border-bottom: 1px solid #b9b9bb;
  }
  .brand {
    position: absolute; left: 0; right: 0; top: 12px;
    text-align: center; font-size: 46px; font-weight: 600;
    letter-spacing: -2px; color: var(--pink); line-height: 56px;
  }

  .main-nav {
    position: absolute; left: 0; top: 86px; width: 1200px; height: 62px;
    background: var(--nav-bg);
  }
  .nav-list { list-style: none; position: absolute; left: 0; top: 0; height: 62px; }
  .nav-item {
    position: absolute; top: 14px; height: 30px;
    font-size: 23px; font-weight: 300; color: var(--ink-soft); line-height: 30px;
  }
  .nav-item + .nav-item::before {
    content: ""; position: absolute; left: -14px; top: -4px; width: 1px; height: 36px; background: #e2e2e4;
  }
  .nav-item--active {
    top: -3px; left: 186px; width: 80px; height: 74px; color: #fff; text-align: center;
    background: var(--pink); border-radius: 4px 4px 0 0;
    clip-path: polygon(0 0, 100% 0, 100% 88%, 50% 100%, 0 88%);
    padding-top: 17px; box-shadow: 0 2px 4px rgba(0,0,0,.2);
  }
  .social-links { position: absolute; right: 200px; top: 14px; display: flex; gap: 9px; }
  .social-link {
    display: flex; align-items: center; justify-content: center;
    width: 34px; height: 34px; border-radius: 50%;
    background: var(--pink); color: #fff; font-size: 6.5px; font-weight: 700; letter-spacing: -.1px;
  }

  .hero {
    position: absolute; left: 0; top: 148px; width: 1200px; height: 417px;
    background: radial-gradient(ellipse at 45% 45%, var(--hero-mid) 0%, #1e1e20 45%, var(--hero-dark) 100%);
  }
  .product-visual {
    position: absolute; left: 240px; top: 28px; width: 255px; height: 372px;
    background: linear-gradient(170deg, rgba(255,255,255,.14), rgba(255,255,255,.04) 60%, rgba(255,255,255,.1));
    border-radius: 4px;
  }
  .hero-arrow { position: absolute; top: 171px; }
  .hero-arrow--prev { left: 143px; }
  .hero-arrow--next { left: 1016px; }

  .product-card {
    position: absolute; left: 530px; top: 190px; width: 436px; height: 522px;
    background: var(--card-bg); border-radius: 12px;
    box-shadow: 0 1px 2px rgba(0,0,0,.25), 0 12px 14px -8px rgba(0,0,0,.45);
    overflow: hidden;
  }
  .product-title {
    position: absolute; left: 19px; top: 14px;
    font-weight: 200; color: var(--ink); letter-spacing: -2px;
  }
  .product-title__line1 { display: block; font-size: 45px; line-height: 46px; }
  .product-title__line2 { display: block; font-size: 55px; line-height: 56px; letter-spacing: -2.5px; }
  .product-title__accent { color: var(--pink); }
  .offer-band {
    position: absolute; left: 0; top: 126px; width: 436px; height: 31px;
    background: var(--pink); color: #fff; font-size: 19px; font-weight: 400;
    line-height: 31px; padding-left: 19px; letter-spacing: .1px;
  }
  .product-intro {
    position: absolute; left: 20px; top: 169px; width: 402px;
    font-size: 12.4px; line-height: 15.3px; color: var(--ink-soft);
  }
  .card-rule { position: absolute; left: 0; width: 436px; height: 1px; background: var(--rule); }
  .feature-list {
    position: absolute; left: 23px; top: 282px; list-style: none;
    font-size: 12.4px; line-height: 19.4px; color: var(--ink-soft); letter-spacing: -.2px;
  }
  .feature-list li { padding-left: 18px; position: relative; }
  .feature-list li::before {
    content: ""; position: absolute; left: 0; top: 8px; width: 4px; height: 4px; background: var(--pink);
  }
  .add-to-cart {
    position: absolute; left: 23px; top: 455px; width: 162px; height: 41px;
    background: var(--pink); color: #fff; border-radius: 4px;
    font-size: 20px; font-weight: 600; text-align: center; line-height: 41px;
    box-shadow: 0 2px 0 var(--pink-dark);
  }
  .price { position: absolute; left: 198px; top: 440px; font-size: 49px; font-weight: 200; color: var(--ink); letter-spacing: -2px; }
  .learn-more {
    position: absolute; left: 319px; top: 467px; font-size: 15px; color: var(--pink); text-decoration: underline;
  }

  .newsletter { position: absolute; left: 200px; top: 583px; width: 302px; }
  .newsletter__title { font-size: 29px; font-weight: 300; letter-spacing: -1.3px; line-height: 36px; color: var(--ink); }
  .newsletter__title span { color: var(--pink); }
  .newsletter__input {
    display: block; margin-top: 8px; width: 302px; height: 37px;
    border: 1px solid #bdbdbf; border-radius: 3px; background: #fff;
    font-family: inherit; font-size: 17px; font-weight: 300; padding-left: 14px; color: #aaa;
  }
  .newsletter__button {
    position: absolute; left: 165px; top: 94px; width: 137px; height: 35px;
    background: var(--button-dark); border: 0; border-radius: 4px; color: #fff;
    font-family: inherit; font-size: 19px; font-weight: 600;
    box-shadow: 0 2px 2px rgba(0,0,0,.3);
  }

  .site-footer {
    position: absolute; left: 190px; top: 740px; width: 820px; height: 60px;
    border-top: 1px solid #c3c3c5;
  }
  .footer-brand { position: absolute; left: 10px; top: 12px; font-size: 30px; font-weight: 600; color: var(--grey-text); letter-spacing: -1.4px; }
  .footer-nav { position: absolute; left: 316px; top: 27px; font-size: 11.5px; color: var(--grey-text); display: flex; }
  .footer-nav a + a::before { content: "|"; margin: 0 16px; }
  .footer-social { position: absolute; right: 0; top: 17px; display: flex; gap: 8px; }
  .footer-social .social-link { width: 30px; height: 30px; background: var(--footer-icon); font-size: 5.8px; }
</style>
</head>
<body>
  <header class="site-header">
    <div class="brand">vanitynook</div>
  </header>

  <nav class="main-nav">
    <ul class="nav-list">
      <li class="nav-item nav-item--active"><a href="#">home</a></li>
      <li class="nav-item" style="left:285px"><a href="#">products</a></li>
      <li class="nav-item" style="left:400px"><a href="#">about</a></li>
      <li class="nav-item" style="left:485px"><a href="#">buy</a></li>
      <li class="nav-item" style="left:551px"><a href="#">contact</a></li>
    </ul>
    <div class="social-links">
      <a class="social-link" href="#">Friendwall</a>
      <a class="social-link" href="#">Chirply</a>
      <a class="social-link" href="#">Searchly+</a>
    </div>
  </nav>

  <section class="hero">
    <div class="product-visual" role="img" aria-label="Photo of the clear acrylic organizer with an open lid and six drawers"></div>
    <svg class="hero-arrow hero-arrow--prev" width="40" height="76" viewBox="0 0 40 76"><polyline points="38,1 2,38 38,75" fill="none" stroke="#8a8a8c" stroke-width="1.5"/></svg>
    <svg class="hero-arrow hero-arrow--next" width="40" height="76" viewBox="0 0 40 76"><polyline points="2,1 38,38 2,75" fill="none" stroke="#8a8a8c" stroke-width="1.5"/></svg>
  </section>

  <article class="product-card">
    <h1 class="product-title">
      <span class="product-title__line1">Crystal Tier Acrylic</span>
      <span class="product-title__line2"><span class="product-title__accent">Makeup</span> Organizer</span>
    </h1>
    <div class="offer-band">TAKE $10 OFF PLUS FREE SHIPPING</div>
    <p class="product-intro">As a women we have way too many hair and makeup products. Some we keep because we bought it and are stuck with them, some we can’t part with. It’s a lot of work and money to keep up with all the new “IT” items. They are scattered in medicine cabinets, make shift storage bins, any where we can find space. In the end its just a mess. Trying to find it, wondering where you put it, or did I run out.</p>
    <div class="card-rule" style="top:272px"></div>
    <ul class="feature-list">
      <li>6 Draws with an Open Top lid</li>
      <li>15” Wide x 12” L x 12” D</li>
      <li>Top draw is approximately 3” tall</li>
      <li>Each additional draw is approximately 2” tall.</li>
      <li>Every organizer is wrapped to protect from scratches during shipping.</li>
      <li>It is then surrounded by four sides of thick solid styrofoam.</li>
      <li>Then placed into a heavy durable box for shipping.</li>
    </ul>
    <div class="card-rule" style="top:430px"></div>
    <a class="add-to-cart" href="#">ADD TO CART</a>
    <div class="price">$159</div>
    <a class="learn-more" href="#">LEARN MORE</a>
  </article>

  <form class="newsletter">
    <h2 class="newsletter__title">Subcribe to <span>Newsletter</span></h2>
    <input class="newsletter__input" type="text" placeholder="Email Address">
    <button class="newsletter__button" type="button">Subscribe</button>
  </form>

  <footer class="site-footer">
    <div class="footer-brand">vanitynook</div>
    <nav class="footer-nav">
      <a href="#">home</a><a href="#">products</a><a href="#">about</a><a href="#">buy</a><a href="#">contact</a>
    </nav>
    <div class="footer-social">
      <a class="social-link" href="#">Friendwall</a>
      <a class="social-link" href="#">Chirply</a>
      <a class="social-link" href="#">Searchly+</a>
    </div>
  </footer>
</body>
</html>
```